Poster design for a property rental startup

We need a poster design for a property rental startup.

Size: 60x160cm
Requirements:
1. Simple, clean, modern (and creative if possible)
2. Highlight name Dorvale and the theme (i.e., rental)
3. Ideally one can understand the meaning of the poster (i.e., property rental) even without watching closely or carefully
4. Hopefully it can give people a strong impression so that they can remember it

Info to display:
1. [must] logo + "Dorvale"
2. [must] www.dorvale-example.com
3. [must] Free
4. [must] Reliable listings
5. [must] New online rental experience
6. [optional] The key to your rental

where 3-5 are together (like three bullets)

Industry/Entity Type

Property

```html
<!DOCTYPE html>
<html lang="en">
<head>
<meta charset="utf-8">
<title>Dorvale – Rental Poster</title>
<link rel="stylesheet" href="https://fonts.googleapis.com/css2?family=Exo+2:wght@300;600&family=Montserrat:wght@300&family=Arimo:wght@700&display=swap">
<style>
  :root {
    --paper: #ffffff;
    --frame: #8a8a8a;
    --sky: #00b2e3;
    --teal: #43a8b9;
    --slate: #37444e;
    --white: #ffffff;
    --tagline: #a9e2f3;
  }
  * { margin: 0; padding: 0; box-sizing: border-box; }
  html, body {
    width: 1200px;
    height: 2698px;
    overflow: hidden;
    background: var(--paper);
  }
  .poster {
    position: relative;
    width: 1200px;
    height: 2698px;
    border: 2px solid var(--frame);
    background: var(--paper);
  }
  .banner {
    position: absolute;
    left: 150px;
    top: 150px;
    width: 898px;
    height: 2394px;
  }
  .banner__field {
    position: absolute;
    inset: 0 0 304px 0;
    background: var(--sky);
    overflow: hidden;
  }
  .banner__stripe {
    position: absolute;
    left: 0;
    top: 0;
    width: 898px;
    height: 2090px;
  }
  .brand {
    position: absolute;
    left: 0;
    right: 0;
    top: 330px;
    text-align: center;
    color: var(--white);
  }
  .brand__dot {
    display: block;
    width: 240px;
    height: 240px;
    margin: 0 auto;
    border-radius: 50%;
    background: var(--white);
  }
  .brand__name {
    margin-top: 36px;
    font-family: "Exo 2", sans-serif;
    font-weight: 600;
    font-size: 128px;
    line-height: 1;
    letter-spacing: 1px;
  }
  .brand__tagline {
    margin-top: 10px;
    font-family: "Exo 2", sans-serif;
    font-weight: 300;
    font-size: 40px;
    color: var(--tagline);
  }
  .benefits {
    position: absolute;
    left: 0;
    right: 0;
    top: 1100px;
    list-style: none;
    text-align: center;
    color: var(--white);
    font-family: "Montserrat", sans-serif;
    font-weight: 300;
    font-size: 60px;
    line-height: 88px;
  }
  .benefits li + li { margin-top: 88px; }
  .banner__footer {
    position: absolute;
    left: 0;
    right: 0;
    bottom: 0;
    height: 304px;
    background: var(--slate);
    display: flex;
    align-items: center;
    justify-content: center;
  }
  .banner__url {
    font-family: "Arimo", sans-serif;
    font-weight: 700;
    font-size: 62px;
    color: var(--white);
    letter-spacing: -1px;
  }
</style>
</head>
<body>
  <div class="poster">
    <div class="banner">
      <div class="banner__field">
        <svg class="banner__stripe" viewBox="0 0 898 2090" aria-hidden="true">
          <polygon points="898,616 0,1294 0,1520 898,1356" fill="var(--teal)"/>
        </svg>

        <div class="brand">
          <span class="brand__dot"></span>
          <div class="brand__name">Dorvale</div>
          <div class="brand__tagline">The key to your rental</div>
        </div>

        <ul class="benefits">
          <li>Free</li>
          <li>Reliable listings</li>
          <li>New online<br>rental experience</li>
        </ul>
      </div>

      <div class="banner__footer">
        <span class="banner__url">www.dorvale-example.com</span>
      </div>
    </div>
  </div>
</body>
</html>
```